Dental Practice - Smiles Ahead - Corvell Walk - requires New Patient Flyer

We need a flyer to tell prospecting new patients about a new patient offer in our practice, Themed with black and whitewith a bit of colour, and using black and white stripes if possible.
We want to look empathetic, modern and appeal to adults.
The offer is for a complete comprehensive dental examination including all necessary x-rays with no out of pocket expense

Target Market(s)

adults, in particular 30-60 year olds

Industry/Entity Type

Dental

Font styles to use
Sans Serif

Colors
000000
ffffff
cee9f5

Requirements
Must have
• Smiles Ahead
• We are located in the heart of city Adelaide, along the iconic Corvell Walk.
• Dentist
• Complete comprehensive dental examination including all necessary x-rays
• with $0 out of pocket expense if you have dental health cover.
• No Health fund? We will do it all for you $95.
• With over 50 years combined experience, Dr Peter Halvorsen and Dr Wesley Tunbridge can offer all areas of dental treatment including Preventative, Whitening, Children, General, Cosmetic, Removal, Sedation and Implants.
• (08) 8564 3097
• frontdesk@brightquaydental.com.au
• Level 2, 17 Corvell Walk Adelaide SA 5000
• Please try and include all 3 pictures attached
Nice to have
• Partner Plus with KOVA, Accept all health funds, claim on the spot with MEDSWIPE
Should not have
• colour red, someone not smiling, someone in pain, photo of bad teeth/smile

```html
<!DOCTYPE html>
<html lang="en">
<head>
<meta charset="utf-8">
<title>Smiles Ahead – New Patient Flyer</title>
<link rel="stylesheet" href="https://fonts.googleapis.com/css2?family=Alegreya:wght@400;700&family=Alegreya+SC:wght@700&family=Arimo:ital,wght@0,400;1,400;1,700&display=swap">
<style>
  :root {
    --ink: #000000;
    --paper: #ffffff;
    --sky: #cee9f5;
    --aqua: #9fe3f2;
    --navy: #1b2a4a;
    --fund-blue: #2a8fd6;
    --panel-blue: #3f7fd0;
    --apple: #8cc63f;
    --map-tone: #e9e4da;
    --photo-tone: #f0d9cc;
    --text-dark: #1a1a1a;
  }
  * { box-sizing: border-box; margin: 0; padding: 0; }
  html, body { width: 848px; height: 1200px; overflow: hidden; }
  body {
    position: relative;
    font-family: "Alegreya", Georgia, serif;
    color: var(--text-dark);
    background: linear-gradient(160deg, var(--aqua) 0%, var(--sky) 30%, var(--paper) 55%, var(--sky) 80%, var(--aqua) 100%);
  }
  .swirls { position: absolute; inset: 0; width: 848px; height: 1200px; }

  .logo-block {
    position: absolute; left: 17px; top: 11px; width: 383px; height: 205px;
    background: var(--ink);
    display: flex; align-items: center; justify-content: center;
  }
  .logo-name { color: var(--paper); font-size: 52px; font-weight: 400; letter-spacing: 1px; }

  .contact-card {
    position: absolute; left: 17px; top: 216px; width: 383px; height: 93px;
    background: var(--paper);
    text-align: center; font-style: normal; font-size: 17.5px; line-height: 23px; padding-top: 12px;
  }

  .practice-tab {
    position: absolute; left: 402px; top: 0; width: 446px; height: 29px;
    background: var(--ink); color: var(--paper);
    text-align: center; font-size: 23px; line-height: 29px;
  }
  .hero-photo {
    position: absolute; left: 402px; top: 29px; width: 446px; height: 284px;
    background: linear-gradient(100deg, var(--apple) 0%, #b5d98a 28%, var(--paper) 48%, var(--photo-tone) 75%, #e7c3b2 100%);
  }
  .hero-tagline {
    position: absolute; left: 510px; top: 238px; width: 240px;
    text-align: center; font-family: "Arimo", Arial, sans-serif; font-style: italic;
    font-size: 21px; line-height: 27px; color: var(--navy);
  }
  .hero-tagline strong { font-weight: 700; }

  .intro { position: absolute; left: 0; width: 848px; color: var(--navy); }
  .intro-lead { top: 326px; left: 43px; font-size: 25px; }
  .intro-names {
    top: 383px; text-align: center; font-family: "Alegreya SC", Georgia, serif;
    font-weight: 700; font-size: 31px; letter-spacing: 1.5px;
  }
  .intro-tail { top: 434px; text-align: center; font-size: 25px; }

  .services {
    position: absolute; left: 29px; top: 481px; width: 342px; height: 312px;
    background: linear-gradient(90deg, var(--sky) 0%, var(--paper) 100%);
    list-style: none; padding: 5px 0 0 30px;
  }
  .services li { font-size: 23.5px; line-height: 40px; color: var(--navy); }
  .tick { margin-right: 12px; }

  .offer {
    position: absolute; background: rgba(255,255,255,0.85);
    font-size: 20px; color: var(--navy);
  }
  .offer-exam { left: 385px; top: 517px; width: 420px; height: 66px; text-align: center; line-height: 29px; padding-top: 4px; }
  .offer-cover { left: 385px; top: 618px; width: 448px; height: 36px; line-height: 36px; padding-left: 8px; }
  .offer-price { left: 385px; top: 658px; width: 448px; height: 36px; line-height: 36px; padding-left: 8px; }

  .map-area {
    position: absolute; left: 378px; top: 740px; width: 453px; height: 266px;
    background: linear-gradient(135deg, var(--map-tone), #f4f1ea);
    border: 1px solid #cfc8bb;
  }

  .round-photo { position: absolute; border-radius: 50%; border: 4px solid var(--paper); }
  .round-smile { left: 15px; top: 778px; width: 170px; height: 170px;
    background: radial-gradient(circle at 45% 55%, var(--paper) 0 30%, #f3b8b5 60%, var(--sky) 100%); }
  .round-child { left: 191px; top: 770px; width: 176px; height: 176px;
    background: radial-gradient(circle at 50% 50%, var(--photo-tone) 0 45%, #8b5a3c 80%, #6e4530 100%); }

  .location-note {
    position: absolute; left: 7px; top: 951px; width: 374px; height: 72px;
    background: var(--paper); text-align: center;
    font-variant: small-caps; font-size: 20px; line-height: 22px; padding: 3px 6px 0;
  }

  .fund-badge {
    position: absolute; left: 7px; top: 1027px; width: 144px; height: 166px;
    background: var(--fund-blue); color: var(--paper); text-align: center;
  }
  .fund-name { font-size: 40px; font-weight: 700; padding-top: 28px; }
  .fund-tier { position: absolute; left: 0; bottom: 0; width: 100%; height: 40px; background: var(--paper);
    color: var(--fund-blue); font-size: 17px; font-weight: 700; line-height: 40px; letter-spacing: 1px; }

  .claims-panel {
    position: absolute; left: 155px; top: 1027px; width: 226px; height: 166px;
    background: linear-gradient(180deg, var(--panel-blue), #2f6cc0);
    color: var(--paper); text-align: center;
    font-variant: small-caps; font-weight: 700; font-size: 22px; line-height: 25px; padding: 6px 28px 0;
  }
  .claims-panel .terminal { display: block; margin-top: 4px; font-size: 24px; }

  .whitening-banner {
    position: absolute; left: 381px; top: 1027px; width: 460px; height: 166px;
    background: linear-gradient(90deg, #3d9be0 0%, #9fd8f2 55%, var(--paper) 100%);
    font-family: "Arimo", Arial, sans-serif; color: var(--paper);
  }
  .whitening-line1 { position: absolute; left: 30px; top: 20px; font-size: 20px; }
  .whitening-line2 { position: absolute; left: 140px; top: 50px; font-size: 16px; }
  .whitening-model {
    position: absolute; right: 0; top: 0; width: 172px; height: 166px;
    background: linear-gradient(180deg, #7a4a30 0%, var(--photo-tone) 45%, var(--paper) 100%);
  }
</style>
</head>
<body>
  <svg class="swirls" viewBox="0 0 848 1200" aria-hidden="true">
    <path d="M0 420 C 250 300, 520 520, 848 380" fill="none" stroke="#ffffff" stroke-width="30" opacity="0.5"/>
    <path d="M0 640 C 300 540, 560 760, 848 620" fill="none" stroke="#ffffff" stroke-width="18" opacity="0.45"/>
    <path d="M0 900 C 220 820, 600 980, 848 860" fill="none" stroke="#9fe3f2" stroke-width="24" opacity="0.5"/>
  </svg>

  <header>
    <div class="logo-block"><span class="logo-name">Smiles Ahead</span></div>
    <address class="contact-card">
      Level 2, 17 Corvell Walk Adelaide SA 5000<br>
      (08) 8564 3097<br>
      frontdesk@brightquaydental.com.au
    </address>
    <div class="practice-tab">Dental Practice</div>
    <div class="hero-photo" role="img" aria-label="Photo of a bright white smile beside a green apple"></div>
    <p class="hero-tagline">Your Perfect Smile<br><strong>Begins Here!</strong></p>
  </header>

  <p class="intro intro-lead">With over 50 years combined experience,</p>
  <p class="intro intro-names">Dr Peter Halvorsen and Dr Wesley Tunbridge</p>
  <p class="intro intro-tail">can offer all areas of dental treatment including</p>

  <ul class="services">
    <li><span class="tick">√</span>Preventative</li>
    <li><span class="tick">√</span>Teeth Whitening</li>
    <li><span class="tick">√</span>Children Dental Care</li>
    <li><span class="tick">√</span>General Dental Care</li>
    <li><span class="tick">√</span>Cosmetic</li>
    <li><span class="tick">√</span>Tooth Removal</li>
    <li><span class="tick">√</span>Sedation and Implants</li>
  </ul>

  <p class="offer offer-exam">√ Complete comprehensive dental examination<br>including all necessary x-rays.</p>
  <p class="offer offer-cover">√ Free Dental treatment with Dental Health Cover</p>
  <p class="offer offer-price">√ We will do it all for you $95, with no Health Fund</p>

  <div class="map-area" role="img" aria-label="Street map of central Adelaide marking 17 Corvell Walk"></div>

  <div class="round-photo round-smile" role="img" aria-label="Photo of a healthy smile with a dental mirror"></div>
  <div class="round-photo round-child" role="img" aria-label="Photo of a smiling child"></div>

  <p class="location-note">We are located in the heart of city Adelaide, along the iconic Corvell Walk</p>

  <footer>
    <div class="fund-badge">
      <div class="fund-name">KOVA</div>
      <div class="fund-tier">PARTNER PLUS</div>
    </div>
    <div class="claims-panel">Accept all health funds, claim on the spot with <span class="terminal">MEDSWIPE</span></div>
    <div class="whitening-banner">
      <span class="whitening-line1">Get “WOW” Whitening</span>
      <span class="whitening-line2">Results. Today.</span>
      <div class="whitening-model" role="img" aria-label="Photo of a smiling woman with white teeth"></div>
    </div>
  </footer>
</body>
</html>
```